Harlowick billboard

Looking to change up a current design

Remove the best pricing in Sevier county

Remove the prices
Make it say 16/20/30/40 yard dumpsters

Remove delivery pick up 7 days a week

Keep current colors

```html
<!DOCTYPE html>
<html lang="en">
<head>
<meta charset="utf-8">
<title>Harlowick Dumpsters Billboard</title>
<link rel="stylesheet" href="https://fonts.googleapis.com/css2?family=Fredoka:wght@600&family=Montserrat:wght@800&display=swap">
<style>
  :root {
    --page: #e9e9ec;
    --night: #0e0e10;
    --night-soft: #2a2a2e;
    --purple: #9b4fd1;
    --purple-deep: #5a2386;
    --white: #ffffff;
    --ink: #2b2b2e;
    --paper-shadow: #c9c9cc;
  }
  * { box-sizing: border-box; margin: 0; padding: 0; }
  html, body {
    width: 1200px; height: 800px; overflow: hidden;
    background: var(--page);
  }
  .billboard {
    position: absolute; left: 0; top: 173px;
    width: 1200px; height: 454px;
    overflow: hidden;
    background: linear-gradient(135deg, var(--night-soft) 0%, var(--night) 45%, #1a1a1d 100%);
  }
  .backdrop-photo {
    position: absolute; inset: 0 0 110px 0;
    background: radial-gradient(ellipse at 55% 40%, rgba(60,62,58,.55) 0%, rgba(14,14,16,0) 70%);
  }
  .brand {
    position: absolute; left: 46px; top: 40px;
    font-family: "Fredoka", sans-serif; font-weight: 600;
    color: var(--white); line-height: 1;
    text-transform: uppercase;
  }
  .brand-name { display: block; font-size: 52px; letter-spacing: 1px; }
  .brand-sub { display: block; font-size: 28px; margin-top: 4px; margin-left: 104px; letter-spacing: 1px; }
  .sizes {
    position: absolute; left: 45px; top: 188px;
    display: flex; gap: 38px;
  }
  .size {
    width: 126px; text-align: center;
    font-family: "Fredoka", sans-serif; font-weight: 600;
    color: var(--white); line-height: 1;
  }
  .size-number, .size-unit {
    display: block;
    text-shadow:
      2px 0 var(--purple), -2px 0 var(--purple), 0 2px var(--purple), 0 -2px var(--purple),
      2px 2px var(--purple), -2px -2px var(--purple), 2px -2px var(--purple), -2px 2px var(--purple);
  }
  .size-number { font-size: 40px; }
  .size-unit { font-size: 30px; margin-top: -2px; }
  .size-label {
    display: inline-block; margin-top: 4px;
    background: var(--purple); border-radius: 6px;
    padding: 4px 6px 3px; font-size: 17px; letter-spacing: .5px;
  }
  .paper-band { position: absolute; left: 0; bottom: 0; width: 1200px; height: 120px; }
  .website {
    position: absolute; left: 46px; top: 378px;
    font-family: "Montserrat", sans-serif; font-weight: 800;
    font-size: 41px; color: var(--ink); letter-spacing: -.5px;
  }
  .truck-photo {
    position: absolute; left: 668px; top: 126px; width: 532px; height: 328px;
    background: linear-gradient(100deg, rgba(255,255,255,0) 0%, #d9d9dc 18%, #f2f2f2 42%, #4a2a6e 62%, #5a2386 78%, #2e2e30 100%);
    border-radius: 4px 0 0 0;
  }
  .phone {
    position: absolute; left: 902px; top: 380px; width: 298px; height: 50px;
    background: var(--purple); border-radius: 6px 0 0 6px;
    display: flex; align-items: center; gap: 10px; padding-left: 12px;
    font-family: "Fredoka", sans-serif; font-weight: 600;
    font-size: 36px; color: var(--white);
  }
  .phone svg { width: 20px; height: 22px; }
</style>
</head>
<body>
  <section class="billboard" aria-label="Harlowick Dumpsters billboard">
    <div class="backdrop-photo" role="img" aria-label="Dark darkened photo of trees and a parked vehicle"></div>

    <div class="brand">
      <span class="brand-name">Harlowick</span>
      <span class="brand-sub">Dumpsters</span>
    </div>

    <ul class="sizes" style="list-style:none">
      <li class="size"><span class="size-number">16</span><span class="size-unit">YARDS</span><span class="size-label">DUMPSTERS</span></li>
      <li class="size"><span class="size-number">20</span><span class="size-unit">YARDS</span><span class="size-label">DUMPSTERS</span></li>
      <li class="size"><span class="size-number">30</span><span class="size-unit">YARDS</span><span class="size-label">DUMPSTERS</span></li>
      <li class="size"><span class="size-number">40</span><span class="size-unit">YARDS</span><span class="size-label">DUMPSTERS</span></li>
    </ul>

    <svg class="paper-band" viewBox="0 0 1200 120" preserveAspectRatio="none" aria-hidden="true">
      <path d="M0 10 L30 6 L55 14 L80 4 L110 12 L140 5 L175 13 L205 3 L240 11 L270 6 L300 14 L335 4 L365 12 L400 6 L430 13 L465 3 L500 11 L530 5 L565 14 L600 6 L630 12 L665 3 L700 10 L735 5 L770 13 L800 4 L835 11 L870 6 L900 14 L935 5 L970 12 L1000 4 L1035 11 L1070 6 L1100 13 L1135 5 L1170 11 L1200 7 L1200 120 L0 120 Z" fill="var(--paper-shadow)"/>
      <path d="M0 16 L30 11 L55 19 L80 9 L110 17 L140 10 L175 18 L205 8 L240 16 L270 11 L300 19 L335 9 L365 17 L400 11 L430 18 L465 8 L500 16 L530 10 L565 19 L600 11 L630 17 L665 8 L700 15 L735 10 L770 18 L800 9 L835 16 L870 11 L900 19 L935 10 L970 17 L1000 9 L1035 16 L1070 11 L1100 18 L1135 10 L1170 16 L1200 12 L1200 120 L0 120 Z" fill="var(--white)"/>
    </svg>

    <p class="website">HARLOWICKDUMPSTERS.COM</p>

    <div class="truck-photo" role="img" aria-label="Photo of a white roll-off truck carrying a purple dumpster"></div>

    <p class="phone">
      <svg viewBox="0 0 24 24" aria-hidden="true"><path fill="var(--white)" d="M6.6 10.8c1.4 2.8 3.8 5.1 6.6 6.6l2.2-2.2c.3-.3.7-.4 1-.2 1.1.4 2.3.6 3.6.6.6 0 1 .4 1 1V20c0 .6-.4 1-1 1C10.6 21 3 13.4 3 4c0-.6.4-1 1-1h3.5c.6 0 1 .4 1 1 0 1.3.2 2.5.6 3.6.1.3 0 .7-.2 1z"/></svg>
      865-555-0142
    </p>
  </section>
</body>
</html>
```